Professional banners for an eyewear company

I have 3 images which need to be made into banners. Size 990 x 370, with a 10 pixel white border at top and bottom of banner.

They all need to be adjusted to make the colours better and less bright.
All will need some writing written on them with a nice serif font.

Banner 1 text: Handcrafted luxury eyewear, with a purpose...
Banner 2 text: Half of our profits go to help malnourished children in India
Banner 3 text: 10% of your first order, use code: First Order

On our homepage these 3 banners will alternate, so they need to look good together.

Tips
Please take a look at the banners on the lunvoreck.com homepage, this is kind of how I want the text to be displayed, and they use good colours.

The backgrounds on Banners 2 & 3 can be changed.
Banner 3 background if you can change to a nice colour, as per lunvoreck.com homepage.
Updates

Hi, just a quick update, thank you for all the designs submitted so far, please keep in mind that the brand is a luxury high-end brand so designs will need to reflect this.

Industry/Entity Type

Eyewear

```html
<!DOCTYPE html>
<html lang="en">
<head>
<meta charset="utf-8">
<title>Eyewear homepage banners</title>
<link href="https://fonts.googleapis.com/css2?family=Sorts+Mill+Goudy&display=swap" rel="stylesheet">
<style>
  :root {
    --page-dark: #231f20;
    --frame-white: #ffffff;
    --amber-light: #fbb530;
    --amber-deep: #e8892a;
    --leaf-light: #6f9a3a;
    --leaf-deep: #2f7437;
    --ink-brown: #2b1d12;
    --ink-green: #1d5f33;
    --cream: #f6f3ec;
    --saffron-wash: #f7b52e;
    --green-wash: #8cc060;
  }
  * { margin: 0; padding: 0; box-sizing: border-box; }
  html, body {
    width: 1064px; height: 1200px; overflow: hidden;
    background: var(--page-dark);
  }
  .banner-stack { position: relative; width: 1064px; height: 1200px; }
  .banner {
    position: absolute; left: 19px; width: 1029px; height: 384px;
    background: var(--frame-white); padding: 10px 0;
  }
  .banner--intro { top: 10px; }
  .banner--offer { top: 395px; }
  .banner--cause { top: 787px; }
  .banner__field { position: relative; width: 100%; height: 364px; overflow: hidden; }

  .banner--intro .banner__field {
    background: radial-gradient(ellipse at 35% 45%, var(--amber-light) 0%, #f5a12a 50%, var(--amber-deep) 100%);
  }
  .banner--offer .banner__field {
    background: radial-gradient(ellipse at 45% 45%, var(--leaf-light) 0%, #4f8636 55%, var(--leaf-deep) 100%);
  }
  .banner--cause .banner__field {
    background:
      radial-gradient(ellipse at 0% 10%, var(--saffron-wash) 0%, rgba(247,181,46,0.35) 18%, rgba(255,255,255,0) 40%),
      radial-gradient(ellipse at 100% 90%, var(--green-wash) 0%, rgba(140,192,96,0.4) 20%, rgba(255,255,255,0) 45%),
      var(--cream);
  }

  .photo { position: absolute; }
  .photo--frames {
    left: 28px; top: 12px; width: 587px; height: 323px;
    background: radial-gradient(ellipse at 50% 50%, #5a3416 0%, #2a1a10 45%, rgba(42,26,16,0) 72%);
  }
  .photo--model {
    left: 620px; top: 21px; width: 307px; height: 343px;
    background: linear-gradient(180deg, #b8613a 0%, #d9a080 35%, #ece6e0 60%, #f4f1ee 100%);
    border-radius: 120px 120px 0 0;
  }
  .photo--child {
    left: 132px; top: 8px; width: 270px; height: 356px;
    background: linear-gradient(180deg, #4a3325 0%, #8a5a3d 40%, #7fb33a 70%, #6ea22e 100%);
    border-radius: 110px 110px 0 0;
  }

  .headline {
    position: absolute; text-align: center;
    font-family: "Sorts Mill Goudy", "Goudy Old Style", Georgia, serif;
    font-weight: 400; -webkit-text-stroke: 0.6px currentColor;
  }
  .headline--intro {
    left: 600px; width: 416px; top: 82px;
    font-size: 42px; line-height: 60px; color: var(--ink-brown);
  }
  .offer {
    position: absolute; left: 80px; width: 520px; top: 80px;
    text-align: center; color: #f4f1ea;
    font-family: "Sorts Mill Goudy", "Goudy Old Style", Georgia, serif;
    -webkit-text-stroke: 0.6px currentColor;
  }
  .offer__figure { display: block; font-size: 76px; line-height: 86px; }
  .offer__line { display: block; font-size: 50px; line-height: 58px; }
  .offer__code {
    display: block; font-size: 20px; line-height: 26px;
    font-variant: small-caps; letter-spacing: 0.5px; -webkit-text-stroke: 0;
  }
  .headline--cause {
    left: 470px; width: 490px; top: 50px;
    font-size: 42px; line-height: 57px; color: var(--ink-green);
  }
</style>
</head>
<body>
<main class="banner-stack">
  <section class="banner banner--intro">
    <div class="banner__field">
      <div class="photo photo--frames" role="img" aria-label="Black handcrafted acetate eyeglass frames with amber lenses, shown at an angle with a reflection"></div>
      <h1 class="headline headline--intro">Handcrafted<br>luxury eyewear,<br>with a purpose...</h1>
    </div>
  </section>

  <section class="banner banner--offer">
    <div class="banner__field">
      <p class="offer">
        <span class="offer__figure">10%</span>
        <span class="offer__line">Off your first order</span>
        <span class="offer__code">use code: First Order</span>
      </p>
      <div class="photo photo--model" role="img" aria-label="Red-haired woman in sunglasses and a polka-dot blouse, looking surprised"></div>
    </div>
  </section>

  <section class="banner banner--cause">
    <div class="banner__field">
      <div class="photo photo--child" role="img" aria-label="Smiling young girl in a green top, resting her chin on her hand"></div>
      <h2 class="headline headline--cause">Half of our profits<br>go to help<br>malnourished children<br>in India</h2>
    </div>
  </section>
</main>
</body>
</html>
```